Design a compelling Varnelo Business Card that will drive people to my site

I want a business card that I can give to people—less to tell them who I am and more to direct them to my website. My website is a portal for Tidewell Aquatics Officials and a place for people who want to become Tidewell Aquatics Officials.
I am uploading my official company logo as well as a business card mockup that I did on my own. Please feel free to completely stray from this design.
I've included a screen recording of the homepage of my website as well.
Target Market(s)
Tidewell Aquatics Officials and people who desire to become one
Contact Information for Business Card
website url
Look and feel
Each slider illustrates characteristics of the customer's brand and the style your logo design should communicate.

```html
<!DOCTYPE html>
<html lang="en">
<head>
<meta charset="utf-8">
<title>Varnelo Business Card</title>
<link rel="stylesheet" href="https://fonts.googleapis.com/css2?family=Work+Sans:ital,wght@0,400;0,500;0,800;1,400&display=swap">
<style>
  :root {
    --bg: #e0e0e0;
    --brand-blue: #3654a1;
    --ink-blue: #2f4a97;
    --pale-blue: #c3cfec;
    --card-white: #ffffff;
    --wash-deep: #35509f;
    --wash-mid: #7f95cf;
    --wash-light: #e3e9f6;
  }
  * { box-sizing: border-box; margin: 0; padding: 0; }
  html, body {
    width: 848px; height: 1200px; overflow: hidden;
    background: var(--bg);
    font-family: "Work Sans", Arial, sans-serif;
  }
  .sheet {
    width: 848px; height: 1200px;
    display: flex; flex-direction: column; align-items: center; justify-content: center;
    gap: 70px;
  }
  .card {
    position: relative;
    width: 600px; height: 342px;
    border-radius: 30px;
    overflow: hidden;
    box-shadow: 0 6px 18px rgba(0,0,0,0.12);
  }

  /* Back side */
  .card--back {
    background: var(--brand-blue);
    color: var(--card-white);
    display: flex; flex-direction: column; align-items: center; justify-content: center;
  }
  .back-mark {
    display: flex; align-items: center; gap: 16px;
  }
  .back-mark__dot {
    width: 30px; height: 30px; border-radius: 50%;
    background: var(--pale-blue);
  }
  .back-mark__name {
    font-size: 80px; font-weight: 500; letter-spacing: -2px; line-height: 1;
    color: var(--card-white);
  }
  .tagline {
    margin-top: 22px;
    font-size: 18px; font-weight: 400; letter-spacing: 0.8px;
    color: var(--card-white);
  }

  /* Front side */
  .card--front { background: var(--card-white); }
  .front-mark {
    position: absolute; left: 78px; top: 58px;
    display: flex; align-items: center; gap: 10px;
  }
  .front-mark__dot {
    width: 14px; height: 14px; border-radius: 50%;
    background: var(--ink-blue);
  }
  .front-mark__name {
    font-size: 40px; font-weight: 500; letter-spacing: -1px; line-height: 1;
    color: var(--ink-blue);
  }
  .contact {
    position: absolute; left: 348px; top: 38px;
    color: var(--ink-blue);
  }
  .contact__name { font-size: 21px; font-weight: 800; }
  .contact__role { font-size: 13px; font-style: italic; margin-top: 3px; }
  .contact__lines { margin-top: 16px; font-size: 18px; line-height: 1.28; letter-spacing: 0.3px; }
  .swimmer-art {
    position: absolute; left: 0; right: 0; bottom: 0; height: 180px;
    background:
      radial-gradient(ellipse 60% 80% at 25% 100%, var(--wash-deep), transparent 70%),
      radial-gradient(ellipse 45% 40% at 68% 45%, var(--wash-deep), transparent 75%),
      linear-gradient(180deg, rgba(255,255,255,0) 0%, var(--wash-light) 35%, var(--wash-mid) 100%);
  }
</style>
</head>
<body>
  <main class="sheet">
    <section class="card card--back">
      <div class="back-mark">
        <span class="back-mark__dot"></span>
        <span class="back-mark__name">Varnelo</span>
      </div>
      <p class="tagline">THE OPEN DOOR FOR POOL OFFICIALS</p>
    </section>

    <section class="card card--front">
      <div class="front-mark">
        <span class="front-mark__dot"></span>
        <span class="front-mark__name">Varnelo</span>
      </div>
      <div class="contact">
        <p class="contact__name">Marcus Delaney</p>
        <p class="contact__role">CEO &amp; Founder</p>
        <p class="contact__lines">
          marcus@varnelo.com<br>
          (555) 014-2273<br>
          www.varnelo.com
        </p>
      </div>
      <div class="swimmer-art" role="img" aria-label="Blue watercolour illustration of a swimmer gliding through splashing water"></div>
    </section>
  </main>
</body>
</html>
```